Bref créative
Stationary - Morvane Advisory
Business Card, Letterhead & Pen Design
Professional
Helmut Draven
Director
Address line 1
Address line 2
Address line 3
Address line 4
Post Code
QRP@QRP.example
For the business card I like the idea of front/back designs, where either there is something which joins the front and back or there is a slightly modified logo on the back... You're call, I'm open to anything here, so if you come up with something just try it out, I'll give everyone feedback where possible!
Please don't just stick my logo on a pen and say "hey, here you go...", for the pen design I'm looking for colours etc and where they are placed on the pen too!
Anything you think would look good!
Image file to show the logo
Extra images (inc psds!) for the logo

```html
<!DOCTYPE html>
<html lang="en">
<head>
<meta charset="utf-8">
<title>Morvane Advisory – Business Card</title>
<link rel="stylesheet" href="https://fonts.googleapis.com/css2?family=Roboto:wght@400;500&display=swap">
<style>
  :root {
    --backdrop: #e6e1da;
    --frost: rgba(255, 255, 255, 0.45);
    --frost-edge: rgba(255, 255, 255, 0.7);
    --card-white: #ffffff;
    --brand-teal: #1d7690;
    --brand-blue: #2aa3d6;
    --brand-blue-deep: #0f6f9f;
    --ink: #333333;
  }
  html, body {
    margin: 0;
    padding: 0;
    width: 1200px;
    height: 958px;
    overflow: hidden;
    background: var(--backdrop);
    font-family: "Roboto", Arial, sans-serif;
  }
  .canvas {
    position: relative;
    width: 1200px;
    height: 958px;
  }
  .card {
    position: absolute;
    width: 512px;
    height: 288px;
    background: var(--frost);
    border: 1px solid var(--frost-edge);
    box-shadow: 0 6px 18px rgba(0, 0, 0, 0.12);
  }
  .card-front { left: 255px; top: 221px; }
  .card-back  { left: 452px; top: 538px; }

  .front-band {
    position: absolute;
    left: 0;
    top: 67px;
    width: 512px;
    height: 150px;
    background: var(--card-white);
    display: flex;
    align-items: center;
    justify-content: center;
  }
  .brand-name {
    font-family: "Roboto", Arial, sans-serif;
    font-weight: 500;
    font-size: 40px;
    letter-spacing: 0.5px;
    color: var(--brand-teal);
    white-space: nowrap;
  }

  .back-band {
    position: absolute;
    left: 0;
    top: 37px;
    width: 512px;
    height: 180px;
    background: var(--card-white);
  }
  .brand-tile {
    position: absolute;
    left: 4px;
    top: 37px;
    width: 202px;
    height: 204px;
    border-radius: 8px;
    background: linear-gradient(160deg, var(--brand-blue) 0%, var(--brand-blue-deep) 100%);
  }
  .contact {
    position: absolute;
    left: 254px;
    top: 50px;
    color: var(--ink);
  }
  .contact-name {
    margin: 0;
    font-size: 20px;
    font-weight: 400;
    color: var(--brand-blue);
  }
  .contact-role {
    margin: 2px 0 0;
    font-size: 13px;
  }
  .contact-address {
    margin: 22px 0 0;
    font-size: 11px;
    line-height: 14px;
    font-style: normal;
  }
  .contact-lines {
    margin: 14px 0 0;
    font-size: 11px;
    line-height: 15px;
  }
  .contact-lines .label { color: var(--brand-blue); }
</style>
</head>
<body>
<main class="canvas">
  <section class="card card-front" aria-label="Card front">
    <div class="front-band">
      <span class="brand-name">Morvane Advisory</span>
    </div>
  </section>

  <section class="card card-back" aria-label="Card back">
    <div class="back-band"></div>
    <div class="brand-tile" role="img" aria-label="Blue brand tile"></div>
    <div class="contact">
      <h1 class="contact-name">Helmut Draven</h1>
      <p class="contact-role">Director</p>
      <address class="contact-address">
        Address line 1, Address line 2, Address line 3<br>
        Address line 4, Post Code
      </address>
      <p class="contact-lines">
        <span class="label">P:</span> 01632 960 222<br>
        <span class="label">E:</span> QRP@QRP.example
      </p>
    </div>
  </section>
</main>
</body>
</html>
```